Web Design Project

We are an IT System Integrator. We provide Norvik 500 ERP System, CRM etc. We also provide hardware, networking servicing. Please look at www.brinquot.com.sg. They provide the same service as us. We like to redesign our web site. I will attached the color that I prefer for reference.

Our website is www.ravdu.com.sg.  It has been created about 14 years ago.  We are trying to revamp it with a new look and information.   The new website must be informative, fast.    I have attached an attachment which show the color that I prefer(brownish golden).   

Our competitor (www.brinquot.com) is carrying the same trade as us.  They have all the informations In their website that we will like to have.  Therefore I recommend you to take a look at my competitor website and have a better   
understanding on the kind of information I would like to have for my new website.

This project is guarantee to the person with the best design.  We can have it guarantee.

Target Market(s)

Corporate and companies

Industry/Entity Type

Hardware

```html
<!DOCTYPE html>
<html lang="en">
<head>
<meta charset="utf-8">
<title>Ravdu Information Systems Pte Ltd</title>
<link rel="stylesheet" href="https://fonts.googleapis.com/css2?family=Questrial&family=Arimo:wght@400;700&family=Open+Sans&display=swap">
<style>
:root{
  --orange:#c8620e;
  --brown:#a85a1f;
  --ink:#1c1c1c;
  --text:#333;
  --neutral:#6a6a6a;
  --muted:#f2f2f2;
  --white:#fff;
}
*{margin:0;padding:0;box-sizing:border-box}
html,body{width:835px;height:1200px;overflow:hidden;background:var(--white)}
body{position:relative;font-family:"Questrial",sans-serif;color:var(--text)}
.abs{position:absolute}
.header{left:0;top:0;width:835px;height:78px;background:linear-gradient(#fff,#f1f1f1)}
.brand{left:98px;top:26px;display:flex;align-items:center;gap:8px}
.brand-square{width:22px;height:22px;background:var(--orange)}
.brand-name{font:16px "Questrial",sans-serif;color:var(--brown)}
.util{right:99px;top:5px;font-size:10px;color:var(--ink)}
.util span{margin:0 4px;color:#777}
.call{right:99px;top:32px;display:flex;gap:8px;align-items:center}
.call em{display:block;font:italic 12px "Open Sans",sans-serif;color:#666}
.call strong{display:block;font:700 17px "Arimo",sans-serif;color:var(--ink);letter-spacing:.3px}
.nav{left:0;top:78px;width:835px;height:33px;background:linear-gradient(#f3a656,#d9781f);display:flex;padding-left:98px}
.nav a{color:var(--white);text-decoration:none;font-size:13.5px;line-height:33px;padding:0 15px;border-right:1px solid rgba(255,255,255,.3)}
.nav a:first-child{padding-left:17px}
.nav a:last-child{border:none}
.hero{left:0;top:111px;width:835px;height:326px;background:linear-gradient(100deg,#8a9aa8 0%,#dcd4cc 30%,#c9d3dc 55%,#6e8190 100%)}
.slide{left:460px;top:200px;width:277px;height:145px;background:rgba(255,255,255,.6)}
.slide h2{background:var(--ink);color:var(--white);font:700 22px "Arimo",sans-serif;padding:6px 10px;height:40px;border-radius:0 20px 0 0}
.slide p{font:12.5px/1.35 "Open Sans",sans-serif;color:var(--ink);padding:8px 12px}
.arrows{left:655px;top:384px;width:82px;height:41px;background:rgba(255,255,255,.5);display:flex}
.arrows svg{width:41px;height:41px}
h3{font:700 17px "Arimo",sans-serif;color:var(--brown)}
.body-text{font-size:10px;line-height:1.33;color:var(--text)}
.more{font-size:10px;color:var(--brown);display:flex;align-items:center;gap:5px;justify-content:flex-end}
.quote{font-size:10px;line-height:1.35}
.cite{font-size:10px;color:var(--brown);text-align:right}
.client{width:65px;height:65px;display:flex;align-items:center;justify-content:center;font-size:10px;color:var(--neutral);text-align:center;background:#eee}
.news{left:541px;width:196px;display:flex;gap:10px}
.date{width:42px;flex:none}
.date b{display:block;height:24px;background:var(--ink);color:var(--white);font:700 15px/24px "Arimo",sans-serif;text-align:center}
.date i{display:block;height:25px;background:var(--orange);color:var(--white);font:700 15px/25px "Arimo",sans-serif;text-align:center;font-style:normal}
.news h4{font:700 9.5px "Arimo",sans-serif;color:var(--ink);margin-bottom:3px}
.news p{font-size:10px;line-height:1.33}
.news p a{color:var(--brown);text-decoration:none}
.partners{left:98px;top:1001px;width:639px;height:97px;border:3px solid var(--muted);background:#f6f6f6;display:flex;align-items:center;justify-content:space-around}
.partners span{font:15px "Questrial",sans-serif;color:var(--neutral)}
.partners .badge{width:46px;height:46px;border-radius:50%;background:#ddd}
.footer{left:0;top:1144px;width:835px;height:56px;background:linear-gradient(#b56a2c,#9e5820)}
.foot-nav{left:98px;top:1158px;font-size:10px;color:var(--white)}
.foot-nav span{margin:0 8px}
.copy{left:98px;top:1175px;font-size:10px;color:var(--white)}
.social{right:97px;top:1164px;display:flex;gap:7px}
.social i{width:18px;height:18px;border-radius:50%;background:var(--white);display:block}
</style>
</head>
<body>
<header class="abs header"></header>
<div class="abs brand"><i class="brand-square"></i><span class="brand-name">Ravdu Information Systems</span></div>
<div class="abs util">Home<span>|</span>Sitemap<span>|</span>Log-Incident<span>|</span>Enquiry<span>|</span>Client Support</div>
<div class="abs call">
  <svg width="14" height="30" viewBox="0 0 14 30"><path d="M4 1h5v8H6q-1 6 0 12h3v8H4Q-1 15 4 1z" fill="#d9781f"/></svg>
  <div><em>Call Us</em><strong>(100) 2468-1357</strong></div>
</div>
<nav class="abs nav"><a>Company</a><a>Products</a><a>Ledgrix</a><a>Services</a><a>Clientele</a><a>Careers</a><a>Infobin</a><a>Contact</a></nav>

<div class="abs hero" role="img" aria-label="Photo of smiling customer support staff wearing headsets in a bright office"></div>
<div class="abs slide">
  <h2>Networking Services</h2>
  <p>Lorem Ipsum is simply dummy text of the printing and typesetting industry. Lorem Ipsum has been the industry's standard dummy text ever since the 1500s, when an unknown printer took a galley of &nbsp;a type</p>
</div>
<div class="abs arrows">
  <svg viewBox="0 0 41 41"><path d="M26 6 16 20.5 26 35" fill="none" stroke="#fff" stroke-width="1.5"/></svg>
  <svg viewBox="0 0 41 41"><path d="M15 6 25 20.5 15 35" fill="none" stroke="#fff" stroke-width="1.5"/></svg>
</div>

<h3 class="abs" style="left:98px;top:466px">Welcome to Ravdu Information Systems Pet Ltd.</h3>
<p class="abs body-text" style="left:98px;top:491px;width:410px">Ravdu Information Systems Pte Ltd (RIS) is professionally managed by a core group of visionaries and technologists with decades of industry experience between them and backed by a team of trained professionals at all levels of operations. Perfection is a way of life at RIS.<br><br>The organization has grown from a small beginning in 1993, to become a company of international repute for reliability. RIS has transformed from an LEDGRIX Reseller to a company providing total IT solutions to companies in Singapore and the Asia region.</p>
<div class="abs more" style="left:400px;top:607px;width:115px">Read More <svg width="12" height="12" viewBox="0 0 12 12"><circle cx="6" cy="6" r="5" fill="none" stroke="#a85a1f" stroke-width="1.4"/><path d="M3.5 6h5M6 3.5 8.5 6 6 8.5" fill="none" stroke="#a85a1f" stroke-width="1.4"/></svg></div>

<h3 class="abs" style="left:98px;top:642px">Testimonials</h3>
<div class="abs client" style="left:98px;top:673px">Hollan Foods</div>
<p class="abs quote" style="left:176px;top:671px;width:332px">"The greatest benefit was that I see no more sulky face or user...they are happy doing away their invoices... They are happier now and there is less turnover...The reports that LEDGRIX generated are more accurate,"</p>
<p class="abs cite" style="left:176px;top:728px;width:339px">-General Manager at Hollan Foods</p>
<div class="abs client" style="left:98px;top:762px">Unita</div>
<p class="abs quote" style="left:176px;top:765px;width:332px">"The professionalism of Ravdu Information Systems and the long-time relationship between Kerrow and Ravdu are major considerations for Unita, Unita Link and Kerrow in choosing the LEDGRIX Accounting Software. Ravdu's customer-focused approach....,"</p>
<p class="abs cite" style="left:176px;top:832px;width:339px">- Project Manager, Information Technology at Unita</p>
<div class="abs client" style="left:98px;top:868px">Pinwheel</div>
<p class="abs quote" style="left:176px;top:868px;width:332px">"We wish to place on record our thanks and appreciation for the prompt service and personal attention provided by Mr Tan Ho Ming from Ravdu Information Systems Pte Ltd. He has exercised his professionalism and knowledge to help us in solving our Ledgrix issues and problems".</p>
<p class="abs cite" style="left:176px;top:938px;width:339px">-Accountant at Pinwheel Pte Ltd</p>

<h3 class="abs" style="left:541px;top:466px">Recent News</h3>
<div class="abs news" style="top:501px"><div class="date"><b>15</b><i>Aug</i></div><div><h4>Expanding the Boundaries</h4><p>You are invited to attend the Expanding the Boundaries with Velora-ERP....<a>[Read More...]</a></p></div></div>
<div class="abs news" style="top:573px"><div class="date"><b>15</b><i>Aug</i></div><div><h4>Expanding the Boundaries</h4><p>You are invited to attend the Expanding the Boundaries with Velora-ERP....<a>[Read More...]</a></p></div></div>
<div class="abs news" style="top:645px"><div class="date"><b>15</b><i>Aug</i></div><div><h4>Expanding the Boundaries</h4><p>You are invited to attend the Expanding the Boundaries with Velora-ERP....<a>[Read More...]</a></p></div></div>
<div class="abs news" style="top:717px"><div class="date"><b>15</b><i>Aug</i></div><div><h4>Expanding the Boundaries</h4><p>You are invited to attend the Expanding the Boundaries with Velora-ERP....<a>[Read More...]</a></p></div></div>
<div class="abs more" style="left:640px;top:775px;width:97px">See All <svg width="12" height="12" viewBox="0 0 12 12"><circle cx="6" cy="6" r="5" fill="none" stroke="#a85a1f" stroke-width="1.4"/><path d="M3.5 6h5M6 3.5 8.5 6 6 8.5" fill="none" stroke="#a85a1f" stroke-width="1.4"/></svg></div>

<h3 class="abs" style="left:541px;top:810px">LEDGRIX</h3>
<div class="abs" style="left:541px;top:837px;width:196px;height:113px;border:3px solid var(--muted);background:#f6f6f6"></div>
<div class="abs" role="img" aria-label="Row of Ledgrix software product boxes" style="left:549px;top:845px;width:180px;height:97px;background:linear-gradient(#e6f0f7,#6aa8d0)"></div>

<h3 class="abs" style="left:98px;top:973px">Our Partners</h3>
<div class="abs partners">
  <i class="badge"></i>
  <span>Norvik</span>
  <span>Norvik Ledgrix ERP</span>
  <span>Trellon</span>
  <span>Hexa</span>
</div>

<footer class="abs footer"></footer>
<div class="abs foot-nav">Home<span>|</span>Company<span>|</span>Products<span>|</span>Ledgrix<span>|</span>Services<span>|</span>Clientele<span>|</span>Careers<span>|</span>Infobin<span>|</span>Contact</div>
<div class="abs copy">Copyright © &nbsp;2013 Ravdu Information Systems Pet Ltd. All Rights Reserved.</div>
<div class="abs social"><i></i><i></i><i></i></div>
</body>
</html>
```